Bramblewick Homes Ostrava Customer Brochure

Need a brochure designed that is clean and minimal that contains our logo, and contact information. Would like an area where we could insert business cards, and slips on both sides of the openings to place sheets of paper in. Would prefer to have the COVER LETTER I have attached printed on one side of the opening.

Target Market(s)

Home buyers

Font styles to use
Sans Serif

Colors

Designer to choose colors to be used in the design.

Requirements
Must have
• Logo, contact info, website, etc. Must be minimal in design and very clean looking.
Nice to have
• Please see above
Should not have
• No stock pictures of homes, builds, etc. Need it to look very clean

```html
<!DOCTYPE html>
<html lang="en">
<head>
<meta charset="utf-8">
<title>Bramblewick Homes Ostrava – Presentation Folder</title>
<link href="https://fonts.googleapis.com/css2?family=Saira+Condensed:wght@500;700&family=Montserrat:wght@300;500&display=swap" rel="stylesheet">
<style>
  :root {
    --stage: #5c5c5e;
    --tan: #b98d5e;
    --tan-light: #caa27a;
    --tan-faint: #a98058;
    --ink: #333335;
    --paper: #ffffff;
    --frame: #d6d6d6;
    --grey-soft: #c9c9c9;
    --label: #f2f2f2;
  }
  html, body { margin: 0; padding: 0; overflow: hidden; }
  body {
    width: 1200px; height: 1200px;
    background: var(--stage);
    display: flex; flex-direction: column; align-items: center; justify-content: center;
    gap: 46px;
    font-family: "Montserrat", sans-serif;
  }
  .spread { display: flex; flex-direction: column; align-items: center; gap: 16px; }
  .spread__panels { display: flex; box-shadow: 0 14px 30px rgba(0,0,0,.35); }
  .panel { display: block; width: 320px; height: 450px; }
  .spread__label {
    color: var(--label); font-weight: 300; font-size: 30px; letter-spacing: 1px; margin: 0;
  }
  .brand { font-family: "Saira Condensed", sans-serif; font-weight: 700; }
  .headline { font-family: "Saira Condensed", sans-serif; }
  .small { font-family: "Montserrat", sans-serif; }
</style>
</head>
<body>

  <section class="spread spread--outside">
    <div class="spread__panels">
      <!-- Back cover -->
      <svg class="panel panel--back" viewBox="0 0 320 450" xmlns="http://www.w3.org/2000/svg">
        <defs>
          <linearGradient id="tanBack" x1="0" y1="0" x2="1" y2="1">
            <stop offset="0" stop-color="#c49a6c"/><stop offset="1" stop-color="#b2875a"/>
          </linearGradient>
          <linearGradient id="backScene" x1="0" y1="0" x2="0" y2="1">
            <stop offset="0" stop-color="#cfa87f"/><stop offset="1" stop-color="#c29a70"/>
          </linearGradient>
        </defs>
        <rect width="320" height="450" fill="url(#tanBack)"/>
        <polygon role="img" aria-label="Faint townhouse street scene in tan tones"
                 points="180,0 0,0 0,390 280,285 280,120" fill="url(#backScene)"/>
        <polyline points="190,0 290,115 290,295 0,402" fill="none" stroke="var(--frame)" stroke-width="3"/>
        <rect x="92" y="220" width="30" height="30" fill="var(--tan-faint)"/>
        <text class="brand" x="128" y="242" font-size="17" fill="var(--tan-faint)">BRAMBLEWICK HOMES</text>
        <g class="small" fill="var(--paper)">
          <text x="40" y="284" font-size="10" font-weight="500">☎ 420-555-0187</text>
          <text x="40" y="298" font-size="7">✉ info@bramblewickhomesostrava.com</text>
          <text x="40" y="310" font-size="7">◎ www.bramblewickhomesostrava.com</text>
          <text x="40" y="322" font-size="7">⌂ 48 orchard lane, ostrava,</text>
          <text x="48" y="332" font-size="7">moravia, czechia</text>
        </g>
      </svg>

      <!-- Front cover -->
      <svg class="panel panel--front" viewBox="0 0 320 450" xmlns="http://www.w3.org/2000/svg">
        <defs>
          <linearGradient id="tanFront" x1="0" y1="0" x2="1" y2="1">
            <stop offset="0" stop-color="#c09468"/><stop offset="1" stop-color="#b2875a"/>
          </linearGradient>
          <linearGradient id="frontScene" x1="0" y1="0" x2="0" y2="1">
            <stop offset="0" stop-color="#ffffff"/><stop offset=".55" stop-color="#f1f1f1"/><stop offset="1" stop-color="#fafafa"/>
          </linearGradient>
        </defs>
        <rect width="320" height="450" fill="url(#tanFront)"/>
        <polyline points="130,0 30,115 30,295 320,405" fill="none" stroke="var(--frame)" stroke-width="3"/>
        <polygon role="img" aria-label="Faint greyscale townhouse street scene"
                 points="140,0 320,0 320,390 40,285 40,120" fill="url(#frontScene)"/>
        <polygon points="320,300 320,390 250,364" fill="var(--grey-soft)"/>
        <rect x="150" y="80" width="60" height="60" fill="var(--ink)"/>
        <text class="brand" x="180" y="176" font-size="26" fill="var(--ink)" text-anchor="middle">BRAMBLEWICK</text>
        <text class="brand" x="180" y="196" font-size="15" fill="var(--ink)" text-anchor="middle" letter-spacing="4">HOMES</text>
        <text class="headline" x="28" y="398" font-size="27" font-weight="500" fill="var(--paper)">Welcome to</text>
        <text class="headline" x="28" y="424" font-size="23" font-weight="700" fill="var(--ink)">BRAMBLEWICK HOMES</text>
        <text class="small" x="28" y="440" font-size="7.2" fill="var(--paper)" letter-spacing="1.6">www.bramblewickhomesostrava.com</text>
      </svg>
    </div>
    <p class="spread__label">OUT SIDE</p>
  </section>

  <section class="spread spread--inside">
    <div class="spread__panels">
      <!-- Inside left -->
      <svg class="panel panel--inside-left" viewBox="0 0 320 450" xmlns="http://www.w3.org/2000/svg">
        <defs>
          <linearGradient id="greyLeft" x1="0" y1="0" x2="1" y2="0">
            <stop offset="0" stop-color="#e4e4e4"/><stop offset="1" stop-color="#c6c6c6"/>
          </linearGradient>
        </defs>
        <rect width="320" height="450" fill="url(#greyLeft)"/>
        <rect x="140" y="310" width="40" height="40" fill="#cdcdcd"/>
        <text class="brand" x="160" y="376" font-size="17" fill="#cdcdcd" text-anchor="middle">BRAMBLEWICK HOMES</text>
      </svg>

      <!-- Inside right with pocket -->
      <svg class="panel panel--inside-right" viewBox="0 0 320 450" xmlns="http://www.w3.org/2000/svg">
        <defs>
          <linearGradient id="pocketTan" x1="0" y1="0" x2="0" y2="1">
            <stop offset="0" stop-color="#d2a97c"/><stop offset="1" stop-color="#c09468"/>
          </linearGradient>
        </defs>
        <rect width="320" height="450" fill="#e9e9e9"/>
        <rect x="8" y="8" width="304" height="300" fill="var(--paper)"/>
        <rect class="pocket" x="0" y="300" width="320" height="150" fill="url(#pocketTan)"/>
        <line x1="0" y1="300" x2="320" y2="300" stroke="#b58a5d" stroke-width="1.5"/>
        <rect x="143" y="330" width="34" height="34" fill="var(--tan-faint)" opacity=".55"/>
        <text class="brand" x="160" y="386" font-size="15" fill="var(--tan-faint)" opacity=".7" text-anchor="middle">BRAMBLEWICK HOMES</text>
      </svg>
    </div>
    <p class="spread__label">INSIDE</p>
  </section>

</body>
</html>
```